integrative health clinic-Medical massage, acupuncture, chiropractic

we like our logo, but are open to new ideas. We need a new card design. We have added chiropractic and acupuncture that we have put under the name of the business. We are an integrative medical clinic

Target Market(s)

General public, athletes

Contact Information for Business Card

Phone 5055583927
Fax 5055583926
Hours Monday-Friday 9-6
Saturday 10-6
The 20% can be smaller on the back

Colors
3176b5
0355a3

Requirements
Must have
• Logo but am open to ideas
Nice to have
• We are an integrated medical clinic but also want to be personable. We want the card fun and inviting

```html
<!DOCTYPE html>
<html lang="en">
<head>
<meta charset="utf-8">
<title>Clearwater Motion Wellness – Business Card</title>
<link href="https://fonts.googleapis.com/css2?family=Lato:wght@400;700;900&family=Roboto+Condensed:wght@400&family=EB+Garamond:ital@1&display=swap" rel="stylesheet">
<style>
  :root {
    --page: #1c1c1c;
    --card-white: #ffffff;
    --card-dark: #3a3a3b;
    --brand-blue: #0355a3;
    --swoosh-blue: #2b46a8;
    --ink: #1a1a1a;
    --muted: #555555;
    --paper-text: #ffffff;
    --figure-tone-a: #6b3a34;
    --figure-tone-b: #bdbdbd;
  }
  * { box-sizing: border-box; margin: 0; padding: 0; }
  html, body { width: 1200px; height: 900px; overflow: hidden; background: var(--page); }
  body { position: relative; font-family: "Lato", sans-serif; }

  .card {
    position: absolute;
    left: 290px;
    width: 620px;
    height: 354px;
    overflow: hidden;
    box-shadow: 0 10px 30px rgba(0,0,0,.5);
  }
  .card--front { top: 70px; background: var(--card-white); }
  .card--back  { top: 476px; background: var(--card-dark); }

  /* front */
  .swoosh { position: absolute; inset: 0; width: 100%; height: 100%; }
  .brand { position: absolute; }
  .brand__name {
    font-family: "Roboto Condensed", sans-serif;
    font-weight: 400;
    font-size: 44px;
    letter-spacing: -0.5px;
    line-height: 1;
    display: flex; align-items: center; gap: 12px;
  }
  .brand__dot { width: 26px; height: 26px; border-radius: 50%; background: var(--brand-blue); flex: none; }
  .brand__tagline {
    font-family: "EB Garamond", serif;
    font-style: italic;
    font-size: 19px;
    margin-left: 40px;
    border-bottom: 1px solid currentColor;
    padding-bottom: 3px;
    display: inline-block;
  }
  .brand__services {
    font-family: "EB Garamond", serif;
    font-style: italic;
    font-size: 13px;
    margin-left: 180px;
    display: block;
    margin-top: 2px;
  }
  .card--front .brand { left: 150px; top: 40px; color: var(--ink); }
  .card--front .brand__services { color: var(--muted); }

  .contact { position: absolute; left: 34px; top: 168px; font-size: 13px; color: var(--ink); }
  .contact__row { display: flex; align-items: center; gap: 9px; margin-bottom: 4px; }
  .contact__row svg { width: 13px; height: 13px; fill: var(--brand-blue); flex: none; }
  .contact__address {
    color: var(--brand-blue); font-weight: 700; font-size: 14px;
    border-bottom: 1px solid var(--ink); padding-bottom: 8px; margin-bottom: 8px;
    display: inline-block;
  }
  .specialty { font-size: 14px; line-height: 1.3; }
  .specialty__label { color: var(--brand-blue); font-weight: 700; display: block; }
  .specialty__list { color: var(--ink); }

  /* back */
  .anatomy-art {
    position: absolute; right: 0; top: 0; width: 330px; height: 354px;
    background: linear-gradient(100deg, rgba(58,58,59,0) 0%, var(--figure-tone-a) 45%, var(--figure-tone-b) 100%);
    opacity: .55;
  }
  .offer { position: absolute; left: 0; right: 0; top: 62px; text-align: center; color: var(--paper-text); }
  .offer__headline { font-weight: 900; font-size: 40px; letter-spacing: 0.5px; text-transform: uppercase; }
  .offer__book {
    display: flex; align-items: center; justify-content: center; gap: 12px;
    font-size: 15px; letter-spacing: 1px; margin-top: 4px;
  }
  .offer__book::before, .offer__book::after { content: ""; width: 60px; height: 1px; background: var(--paper-text); }
  .offer__url { font-size: 14px; margin-top: 2px; }
  .card--back .brand { left: 170px; top: 190px; color: var(--paper-text); }
  .card--back .brand__name { font-size: 36px; }
  .card--back .brand__dot { width: 22px; height: 22px; background: var(--paper-text); }
  .card--back .brand__tagline { font-size: 16px; margin-left: 34px; }
  .card--back .brand__services { font-size: 11px; margin-left: 150px; }
  .insurance {
    position: absolute; left: 60px; right: 60px; bottom: 28px;
    border-top: 1px solid var(--paper-text); padding-top: 8px;
    text-align: center; color: var(--paper-text); font-weight: 700; font-size: 14px;
  }
</style>
</head>
<body>

<section class="card card--front" aria-label="Card front">
  <svg class="swoosh" viewBox="0 0 620 354" preserveAspectRatio="none" aria-hidden="true">
    <path d="M0 354 L0 330 C180 322 420 250 620 150 L620 180 C440 270 220 340 120 354 Z" fill="#2b46a8"/>
    <path d="M250 300 C400 260 520 200 620 140 L620 150 C520 206 400 264 250 300 Z" fill="#1a1a1a"/>
    <path d="M0 354 L0 340 C200 334 440 270 620 180 L620 354 Z" fill="#2b46a8"/>
    <path d="M0 354 L0 336 C180 328 420 256 620 160 L620 168 C430 264 190 340 0 350 Z" fill="#ffffff"/>
  </svg>

  <div class="brand">
    <div class="brand__name"><span class="brand__dot"></span>Clearwater Motion Wellness</div>
    <span class="brand__tagline">Sports Therapy and Wellness Center</span>
    <span class="brand__services">Chiropractic &amp; Acupuncture</span>
  </div>

  <div class="contact">
    <div class="contact__row">
      <svg viewBox="0 0 24 24"><path d="M6.6 10.8a15 15 0 0 0 6.6 6.6l2.2-2.2a1 1 0 0 1 1-.25 11.4 11.4 0 0 0 3.6.57 1 1 0 0 1 1 1V20a1 1 0 0 1-1 1A17 17 0 0 1 3 4a1 1 0 0 1 1-1h3.5a1 1 0 0 1 1 1c0 1.25.2 2.45.57 3.57a1 1 0 0 1-.25 1z"/></svg>
      <span>(505) 558-3927</span>
    </div>
    <div class="contact__row">
      <svg viewBox="0 0 24 24"><path d="M2 5h20v14H2z M2 5l10 8 10-8" fill="none" stroke="#0355a3" stroke-width="2.2"/></svg>
      <span>info@clearwatermotionnm.com</span>
    </div>
    <span class="contact__address">418 Alder Row, B4 Linden, NM 87000</span>
    <p class="specialty">
      <span class="specialty__label">Specializing in:</span>
      <span class="specialty__list">Medical, Sports Massage &amp; Manual Therapies</span>
    </p>
  </div>
</section>

<section class="card card--back" aria-label="Card back">
  <div class="anatomy-art" role="img" aria-label="Anatomical illustration of a running figure showing muscles"></div>

  <div class="offer">
    <p class="offer__headline">20% off first visit</p>
    <p class="offer__book">BOOK ONLINE</p>
    <p class="offer__url">www.clearwatermotionnm.com</p>
  </div>

  <div class="brand">
    <div class="brand__name"><span class="brand__dot"></span>Clearwater Motion Wellness</div>
    <span class="brand__tagline">Sports Therapy and Wellness Center</span>
    <span class="brand__services">Chiropractic &amp; Acupuncture</span>
  </div>

  <p class="insurance">We accept some isurances, Worker's Comp &amp; Personal Injury</p>
</section>

</body>
</html>
```